Velorak app icon design

We are building an Velorak app and would like some good looking icons to replace the boring ones we have created ourselves.

Please see attached screen shots.

The icons toggle "Active/Inactive" where the inactive is shaded out.

Building

```html
<!DOCTYPE html>
<html lang="en">
<head>
<meta charset="utf-8">
<title>Velorak search screens</title>
<link href="https://fonts.googleapis.com/css2?family=Arimo:wght@400;700&display=swap" rel="stylesheet">
<style>
:root{
  --page:#ffffff;
  --status:#0a0a0a;
  --nav-top:#3a7cc4;
  --nav-bottom:#0c4690;
  --home-btn:#1d5aa6;
  --label:#1f2a36;
  --search-top:#d3d9e0;
  --search-bottom:#aeb8c4;
  --field:#ffffff;
  --field-edge:#8f9aa6;
  --list-bg:#dfe2e6;
  --row:#ffffff;
  --row-line:#c9ced4;
  --text:#1c1c1c;
  --empty:#ececec;
  --kb-top:#c3c7cd;
  --kb-bottom:#9aa0a9;
  --key:#fbfbfb;
  --key-dark:#8d95a1;
  --key-text:#1a1a1a;
}
*{box-sizing:border-box;margin:0;padding:0}
html,body{width:1200px;height:719px;overflow:hidden;background:var(--page)}
body{position:relative;font-family:"Arimo",Helvetica,Arial,sans-serif}
.screen{position:absolute;top:45px;width:344px;height:615px;overflow:hidden;background:var(--list-bg)}
.screen--typing{left:64px}
.screen--results{left:430px}
.screen--owner{left:800px}

.status-bar{height:22px;background:var(--status);color:#fff;font-size:11px;display:flex;align-items:center;justify-content:space-between;padding:0 6px;position:relative}
.status-bar .carrier{display:flex;align-items:center;gap:4px}
.status-bar .time{position:absolute;left:0;right:0;text-align:center;pointer-events:none}
.status-bar .power{display:flex;align-items:center;gap:4px}
.battery{width:22px;height:10px;border:1px solid #fff;border-radius:2px;position:relative}
.battery::after{content:"";position:absolute;right:-3px;top:2px;width:2px;height:4px;background:#fff}
.battery span{display:block;height:100%;background:#fff}

.nav-bar{height:48px;background:linear-gradient(var(--nav-top),var(--nav-bottom));position:relative;display:flex;align-items:center;justify-content:center}
.nav-bar .home{position:absolute;left:7px;top:10px;height:28px;width:46px;border-radius:5px;background:var(--home-btn);border:1px solid #0a3a78;color:#fff;font-size:12px;font-weight:700;display:flex;align-items:center;justify-content:center;box-shadow:inset 0 1px 0 rgba(255,255,255,.3)}
.nav-bar .title{color:#fff;font-size:20px;font-weight:700}

.filter-row{height:85px;background:#fff;display:flex;justify-content:space-between;padding:3px 1px 0}
.filter{width:68px;display:flex;flex-direction:column;align-items:center}
.filter svg{width:66px;height:66px;filter:drop-shadow(0 2px 2px rgba(0,0,0,.3))}
.filter .label{font-size:11px;color:var(--label);margin-top:1px;white-space:nowrap}
.filter--off svg{opacity:.4;filter:grayscale(1)}
.filter--off .label{color:#8a929c}

.search-bar{height:42px;background:linear-gradient(var(--search-top),var(--search-bottom));border-bottom:1px solid #8a95a1;padding:8px 7px}
.search-field{height:26px;background:var(--field);border:1px solid var(--field-edge);border-radius:13px;display:flex;align-items:center;padding:0 6px;gap:6px;font-size:14px;color:var(--text)}
.search-field .query{flex:1}

.result-list{position:absolute;left:0;right:0;top:197px;bottom:0;overflow:hidden}
.result-list .track{position:absolute;left:3px;right:3px}
.result{height:52px;background:var(--row);border-bottom:1px solid var(--row-line);border-radius:4px;margin-bottom:2px;display:flex;align-items:center;padding:0 8px 0 2px;gap:8px}
.result svg.badge{width:38px;height:38px;flex:none;filter:drop-shadow(0 1px 1px rgba(0,0,0,.3))}
.result .text{flex:1;font-size:14.5px;line-height:17px;color:var(--text);white-space:nowrap;overflow:hidden}
.result .chev{width:8px;height:13px;flex:none}

.empty{position:absolute;left:0;right:0;top:197px;height:187px;background:var(--empty)}
.keyboard{position:absolute;left:0;right:0;top:384px;bottom:0;background:linear-gradient(var(--kb-top),var(--kb-bottom));padding:9px 3px 0}
.kb-row{display:flex;justify-content:center;gap:5px;margin-bottom:15px}
.key{height:41px;width:29px;background:var(--key);border-radius:5px;box-shadow:0 1px 1px rgba(0,0,0,.45);display:flex;align-items:center;justify-content:center;font-size:20px;color:var(--key-text)}
.key--wide{width:40px;background:var(--key-dark);color:#fff;font-size:13px}
.key--space{width:148px;font-size:14px;color:#555;background:#e4e6e9}
.key--go{width:96px;background:var(--key-dark);color:#c9ced6;font-size:14px}
.kb-row--mid{padding:0 16px}
</style>
</head>
<body>

<svg width="0" height="0" style="position:absolute" aria-hidden="true">
  <defs>
    <radialGradient id="disc-fill" cx="50%" cy="35%" r="65%">
      <stop offset="0" stop-color="#2f73c4"/>
      <stop offset=".65" stop-color="#16508f"/>
      <stop offset="1" stop-color="#0b3466"/>
    </radialGradient>
    <linearGradient id="disc-ring" x1="0" y1="0" x2="0" y2="1">
      <stop offset="0" stop-color="#ffffff"/>
      <stop offset="1" stop-color="#b9c8da"/>
    </linearGradient>
    <linearGradient id="gloss" x1="0" y1="0" x2="0" y2="1">
      <stop offset="0" stop-color="#ffffff" stop-opacity=".55"/>
      <stop offset="1" stop-color="#ffffff" stop-opacity="0"/>
    </linearGradient>
    <linearGradient id="glyph" x1="0" y1="0" x2="0" y2="1">
      <stop offset="0" stop-color="#ffffff"/>
      <stop offset="1" stop-color="#dbe5f1"/>
    </linearGradient>
    <symbol id="disc" viewBox="0 0 40 40">
      <circle cx="20" cy="20" r="19.2" fill="url(#disc-ring)"/>
      <circle cx="20" cy="20" r="17.6" fill="url(#disc-fill)"/>
    </symbol>
    <symbol id="shine" viewBox="0 0 40 40">
      <ellipse cx="20" cy="11" rx="13" ry="8" fill="url(#gloss)"/>
    </symbol>
    <symbol id="i-case" viewBox="0 0 40 40">
      <use href="#disc"/>
      <path d="M15.5 14 V11.5 a1.5 1.5 0 0 1 1.5-1.5 h6 a1.5 1.5 0 0 1 1.5 1.5 V14" fill="none" stroke="#fff" stroke-width="1.8"/>
      <rect x="8.5" y="14" width="23" height="15.5" rx="2.5" fill="url(#glyph)"/>
      <path d="M8.5 20.5 H31.5" stroke="#16508f" stroke-width="1.2"/>
      <rect x="18" y="19" width="4" height="3.2" rx=".8" fill="#16508f"/>
      <use href="#shine"/>
    </symbol>
    <symbol id="i-house" viewBox="0 0 40 40">
      <use href="#disc"/>
      <rect x="25" y="10" width="3" height="6" fill="url(#glyph)"/>
      <path d="M20 8.5 L33 20 H29.5 V31 H10.5 V20 H7 Z" fill="url(#glyph)" stroke-linejoin="round"/>
      <path d="M17 31 V24.5 a3 3 0 0 1 6 0 V31 Z" fill="#16508f"/>
      <use href="#shine"/>
    </symbol>
    <symbol id="i-owner" viewBox="0 0 40 40">
      <use href="#disc"/>
      <circle cx="20" cy="14" r="5.6" fill="url(#glyph)"/>
      <path d="M9 32 C9 24.5 13 21 20 21 C27 21 31 24.5 31 32 Z" fill="url(#glyph)"/>
      <path d="M18.3 21 L21.7 21 L20.9 23 L22 29 L20 31.5 L18 29 L19.1 23 Z" fill="#16508f"/>
      <use href="#shine"/>
    </symbol>
    <symbol id="i-tenant" viewBox="0 0 40 40">
      <use href="#disc"/>
      <circle cx="20" cy="14" r="5.6" fill="url(#glyph)"/>
      <path d="M9 32 C9 24.5 13 21 20 21 C27 21 31 24.5 31 32 Z" fill="url(#glyph)"/>
      <use href="#shine"/>
    </symbol>
    <symbol id="i-staff" viewBox="0 0 40 40">
      <use href="#disc"/>
      <circle cx="12" cy="16" r="3.8" fill="#dbe5f1"/>
      <path d="M5 29 C5 23 8 21 12 21 C16 21 19 23 19 29 Z" fill="#dbe5f1"/>
      <circle cx="28" cy="16" r="3.8" fill="#dbe5f1"/>
      <path d="M21 29 C21 23 24 21 28 21 C32 21 35 23 35 29 Z" fill="#dbe5f1"/>
      <circle cx="20" cy="14" r="4.8" fill="#fff" stroke="#16508f" stroke-width="1.1"/>
      <path d="M11.5 31 C11.5 24 15 21.5 20 21.5 C25 21.5 28.5 24 28.5 31 Z" fill="#fff" stroke="#16508f" stroke-width="1.1"/>
      <use href="#shine"/>
    </symbol>
    <symbol id="chev" viewBox="0 0 8 13">
      <path d="M1.5 1.5 L6.5 6.5 L1.5 11.5" fill="none" stroke="#9aa1a9" stroke-width="1.6"/>
    </symbol>
    <symbol id="glass" viewBox="0 0 14 14">
      <circle cx="5.5" cy="5.5" r="4" fill="none" stroke="#6b7480" stroke-width="1.6"/>
      <path d="M8.5 8.5 L12.5 12.5" stroke="#6b7480" stroke-width="1.8"/>
    </symbol>
    <symbol id="clear" viewBox="0 0 16 16">
      <circle cx="8" cy="8" r="7.5" fill="#9aa1aa"/>
      <path d="M5 5 L11 11 M11 5 L5 11" stroke="#fff" stroke-width="1.6"/>
    </symbol>
    <symbol id="bars" viewBox="0 0 30 8">
      <circle cx="3" cy="4" r="2.4" fill="#fff"/><circle cx="9" cy="4" r="2.4" fill="#fff"/><circle cx="15" cy="4" r="2.4" fill="#fff"/>
      <circle cx="21" cy="4" r="2.2" fill="none" stroke="#fff" stroke-width=".8"/><circle cx="27" cy="4" r="2.2" fill="none" stroke="#fff" stroke-width=".8"/>
    </symbol>
    <symbol id="wifi" viewBox="0 0 12 10">
      <path d="M1 3.5 Q6 -1 11 3.5 M3 5.8 Q6 3 9 5.8" fill="none" stroke="#fff" stroke-width="1.3"/>
      <circle cx="6" cy="8.2" r="1.2" fill="#fff"/>
    </symbol>
    <symbol id="bt" viewBox="0 0 8 12">
      <path d="M1 3.5 L6.5 8.5 L4 11 L4 1 L6.5 3.5 L1 8.5" fill="none" stroke="#bbb" stroke-width="1"/>
    </symbol>
  </defs>
</svg>

<section class="screen screen--typing">
  <div class="status-bar">
    <span class="carrier"><svg width="30" height="8"><use href="#bars"/></svg>Nexalink<svg width="12" height="10"><use href="#wifi"/></svg></span>
    <span class="time">15:45</span>
    <span class="power"><svg width="8" height="12"><use href="#bt"/></svg>5%<span class="battery"><span style="width:8%"></span></span></span>
  </div>
  <div class="nav-bar"><span class="home">Home</span><span class="title">Search</span></div>
  <div class="filter-row">
    <div class="filter"><svg><use href="#i-case"/></svg><span class="label">My Portfolio</span></div>
    <div class="filter"><svg><use href="#i-house"/></svg><span class="label">Property</span></div>
    <div class="filter"><svg><use href="#i-owner"/></svg><span class="label">Owner</span></div>
    <div class="filter"><svg><use href="#i-tenant"/></svg><span class="label">Tenant</span></div>
    <div class="filter"><svg><use href="#i-staff"/></svg><span class="label">Staff</span></div>
  </div>
  <div class="search-bar"><div class="search-field"><svg width="14" height="14"><use href="#glass"/></svg><span class="query"></span></div></div>
  <div class="empty"></div>
  <div class="keyboard">
    <div class="kb-row"><span class="key">Q</span><span class="key">W</span><span class="key">E</span><span class="key">R</span><span class="key">T</span><span class="key">Y</span><span class="key">U</span><span class="key">I</span><span class="key">O</span><span class="key">P</span></div>
    <div class="kb-row kb-row--mid"><span class="key">A</span><span class="key">S</span><span class="key">D</span><span class="key">F</span><span class="key">G</span><span class="key">H</span><span class="key">J</span><span class="key">K</span><span class="key">L</span></div>
    <div class="kb-row"><span class="key key--wide">⇧</span><span class="key">Z</span><span class="key">X</span><span class="key">C</span><span class="key">V</span><span class="key">B</span><span class="key">N</span><span class="key">M</span><span class="key key--wide">⌫</span></div>
    <div class="kb-row"><span class="key key--wide">123</span><span class="key key--wide">●</span><span class="key key--space">space</span><span class="key key--go">Search</span></div>
  </div>
</section>

<section class="screen screen--results">
  <div class="status-bar">
    <span class="carrier"><svg width="30" height="8"><use href="#bars"/></svg>Nexalink<svg width="12" height="10"><use href="#wifi"/></svg></span>
    <span class="time">15:49</span>
    <span class="power"><svg width="8" height="12"><use href="#bt"/></svg>8%<span class="battery"><span style="width:12%"></span></span></span>
  </div>
  <div class="nav-bar"><span class="home">Home</span><span class="title">Search</span></div>
  <div class="filter-row">
    <div class="filter"><svg><use href="#i-case"/></svg><span class="label">All</span></div>
    <div class="filter"><svg><use href="#i-house"/></svg><span class="label">Property</span></div>
    <div class="filter"><svg><use href="#i-owner"/></svg><span class="label">Owner</span></div>
    <div class="filter"><svg><use href="#i-tenant"/></svg><span class="label">Tenant</span></div>
    <div class="filter"><svg><use href="#i-staff"/></svg><span class="label">Staff</span></div>
  </div>
  <div class="search-bar"><div class="search-field"><svg width="14" height="14"><use href="#glass"/></svg><span class="query">Main</span><svg width="16" height="16"><use href="#clear"/></svg></div></div>
  <div class="result-list"><div class="track" style="top:-10px">
    <div class="result"><svg class="badge"><use href="#i-house"/></svg><span class="text">4/12 Harlow St<br>WESTBRIDGE EAST NSW 2190</span><svg class="chev"><use href="#chev"/></svg></div>
    <div class="result"><svg class="badge"><use href="#i-house"/></svg><span class="text">6/108 Corran Street<br>WESTBRIDGE NSW 2190</span><svg class="chev"><use href="#chev"/></svg></div>
    <div class="result"><svg class="badge"><use href="#i-house"/></svg><span class="text">Tallis 604/22 Sir Edwin Hale<br>Cresent</span><svg class="chev"><use href="#chev"/></svg></div>
    <div class="result"><svg class="badge"><use href="#i-owner"/></svg><span class="text">Nadia Corwell for Trustee For Ndc<br>Mainenance Tr</span><svg class="chev"><use href="#chev"/></svg></div>
    <div class="result"><svg class="badge"><use href="#i-owner"/></svg><span class="text">Nadia Corwell Trustee For Ndc<br>Maintenance</span><svg class="chev"><use href="#chev"/></svg></div>
    <div class="result"><svg class="badge"><use href="#i-tenant"/></svg><span class="text">KTR Building Maintenance &amp;<br>Electrical Service P/L</span><svg class="chev"><use href="#chev"/></svg></div>
    <div class="result"><svg class="badge"><use href="#i-tenant"/></svg><span class="text">Tharani, Devan Pal</span><svg class="chev"><use href="#chev"/></svg></div>
    <div class="result"><svg class="badge"><use href="#i-tenant"/></svg><span class="text">Ren Tharani, Mirela</span><svg class="chev"><use href="#chev"/></svg></div>
  </div></div>
</section>

<section class="screen screen--owner">
  <div class="status-bar">
    <span class="carrier"><svg width="30" height="8"><use href="#bars"/></svg>Nexalink<svg width="12" height="10"><use href="#wifi"/></svg></span>
    <span class="time">15:50</span>
    <span class="power"><svg width="8" height="12"><use href="#bt"/></svg>8%<span class="battery"><span style="width:12%"></span></span></span>
  </div>
  <div class="nav-bar"><span class="home">Home</span><span class="title">Search</span></div>
  <div class="filter-row">
    <div class="filter filter--off"><svg><use href="#i-case"/></svg><span class="label">All</span></div>
    <div class="filter"><svg><use href="#i-house"/></svg><span class="label">Property</span></div>
    <div class="filter"><svg><use href="#i-owner"/></svg><span class="label">Owner</span></div>
    <div class="filter"><svg><use href="#i-tenant"/></svg><span class="label">Tenant</span></div>
    <div class="filter"><svg><use href="#i-staff"/></svg><span class="label">Staff</span></div>
  </div>
  <div class="search-bar"><div class="search-field"><svg width="14" height="14"><use href="#glass"/></svg><span class="query">Main</span><svg width="16" height="16"><use href="#clear"/></svg></div></div>
  <div class="result-list"><div class="track" style="top:-14px">
    <div class="result"><svg class="badge"><use href="#i-house"/></svg><span class="text">16/16 Ashdown Street<br>WESTBRIDGE NSW 2190</span><svg class="chev"><use href="#chev"/></svg></div>
    <div class="result"><svg class="badge"><use href="#i-house"/></svg><span class="text">10/15 Pellow Street<br>WESTBRIDGE EAST NSW 2190</span><svg class="chev"><use href="#chev"/></svg></div>
    <div class="result"><svg class="badge"><use href="#i-house"/></svg><span class="text">57 Fenwick Street<br>WESTBRIDGE NSW 2190</span><svg class="chev"><use href="#chev"/></svg></div>
    <div class="result"><svg class="badge"><use href="#i-house"/></svg><span class="text">4/12 Harlow St<br>WESTBRIDGE EAST NSW 2190</span><svg class="chev"><use href="#chev"/></svg></div>
    <div class="result"><svg class="badge"><use href="#i-house"/></svg><span class="text">6/108 Corran Street<br>WESTBRIDGE NSW 2190</span><svg class="chev"><use href="#chev"/></svg></div>
    <div class="result"><svg class="badge"><use href="#i-house"/></svg><span class="text">Tallis 604/22 Sir Edwin Hale<br>Cresent</span><svg class="chev"><use href="#chev"/></svg></div>
    <div class="result"><svg class="badge"><use href="#i-tenant"/></svg><span class="text">KTR Building Maintenance &amp;<br>Electrical Service P/L</span><svg class="chev"><use href="#chev"/></svg></div>
    <div class="result"><svg class="badge"><use href="#i-tenant"/></svg><span class="text">Tharani, Devan Pal</span><svg class="chev"><use href="#chev"/></svg></div>
  </div></div>
</section>

</body>
</html>
```